Endocrinologist needs new stationery

I have a logo from MarkForge and now need stationery with the new logo.

Address: Suite 4, 282 Falcon Street, Richmond, VIC 3121
Phone: 03 9417 2253
Fax: 03 9417 2255
Website: www.drmaylacorwen.com.au
Email: admin@drmaylacorwen.com.au

```html
<!DOCTYPE html>
<html lang="en">
<head>
<meta charset="utf-8">
<title>Dr Mayla Corwen — Stationery</title>
<link href="https://fonts.googleapis.com/css2?family=Source+Serif+4:wght@400;600&display=swap" rel="stylesheet">
<style>
:root{
  --bg:#e7e8ea;
  --paper:#ffffff;
  --blue:#306f9e;
  --plum:#735468;
  --ink:#4a4a4a;
  --muted:#9a9a9a;
  --rule:#b9b9b9;
}
*{box-sizing:border-box;margin:0;padding:0}
html,body{width:1029px;height:1200px;overflow:hidden;background:var(--bg)}
body{position:relative;font-family:"Source Serif 4",Georgia,serif;color:var(--ink)}
.sheet{position:absolute;background:var(--paper);overflow:hidden}
.wave{position:absolute;left:0;bottom:0;width:100%}
.brand{position:absolute;color:var(--blue);font-weight:400;white-space:nowrap;line-height:1}
.contact{position:absolute;font-size:3.6px;line-height:6.6px;color:var(--ink);list-style:none}
.contact li{display:flex;align-items:center;gap:4px}
.contact.right li{justify-content:flex-end}
.icon{width:4px;height:4px;flex:none}
.icon path,.icon circle,.icon rect{fill:none;stroke:var(--blue);stroke-width:1.6}

/* envelopes */
.envelope-back{left:117px;top:54px;width:368px;height:183px}
.envelope-front{left:558px;top:54px;width:368px;height:183px}
.envelope-flap{position:absolute;left:0;top:0;width:100%;height:56px}

/* business cards */
.card-front{left:49px;top:329px;width:225px;height:129px}
.card-back{left:49px;top:505px;width:225px;height:129px}
.portrait{position:absolute;left:45px;top:24px;width:46px;height:46px;border-radius:50%;border:2px solid var(--blue);background:radial-gradient(circle at 50% 40%,#d9c3a8,#6f8aa6 70%)}

/* letters */
.letter-patient{left:338px;top:289px;width:275px;height:389px}
.letter-general{left:686px;top:289px;width:275px;height:389px}
.doctor-block{position:absolute;font-size:3.6px;line-height:5px}
.doctor-block .name{color:var(--blue);font-weight:600;font-size:6px;line-height:8px}
.doctor-block .role{color:var(--muted)}
.patient-fields{position:absolute;left:21px;top:82px;width:234px;display:flex;gap:3px;font-size:4px;color:var(--plum);align-items:flex-end}
.patient-fields .line{flex:1;border-bottom:0.5px dotted var(--rule);margin-bottom:1px}
.recipient{position:absolute;font-size:5.4px;line-height:7px}
.recipient .name{color:var(--blue);font-weight:600}
.recipient .role{color:var(--muted);font-size:4.4px}
.date{position:absolute;font-size:4px;color:var(--ink)}
.body-copy{position:absolute;font-size:4.4px;line-height:9.3px;text-align:justify;color:var(--ink)}
.body-copy p+p{margin-top:9px}
.signature{position:absolute;background:linear-gradient(90deg,#c9d8e7,#9fbad6);border-radius:2px}
.sign-role{position:absolute;font-size:5.6px;color:var(--muted);text-align:center}
.address-foot{position:absolute;font-size:5.4px;line-height:6.4px;color:var(--muted);text-align:center}

/* folder */
.folder{left:213px;top:719px;width:603px;height:426px}
.folder-insert{position:absolute;left:319px;top:28px;width:261px;height:340px;background:var(--paper);box-shadow:0 0 3px rgba(0,0,0,.18)}
.pocket{position:absolute;top:316px;height:110px;background:var(--paper)}
.pocket-left{left:0;width:288px;border-top-right-radius:26px;box-shadow:2px -2px 4px rgba(0,0,0,.12)}
.pocket-right{left:302px;width:301px;border-top-left-radius:26px;box-shadow:-2px -2px 4px rgba(0,0,0,.12)}
.pocket-gap{position:absolute;left:280px;top:340px;width:30px;height:86px}
</style>
</head>
<body>

<!-- envelope back with flap -->
<section class="sheet envelope-back">
  <svg class="envelope-flap" viewBox="0 0 368 56" preserveAspectRatio="none" aria-hidden="true">
    <path d="M0 0 L15 48 Q18 55 28 55 H338 Q348 55 352 48 L368 0" fill="#fff" stroke="#cfcfcf" stroke-width="0.8"/>
  </svg>
  <div class="brand" style="left:116px;top:22px;font-size:17px">Dr Mayla Corwen</div>
  <ul class="contact" style="left:21px;top:111px">
    <li><svg class="icon" viewBox="0 0 10 10"><path d="M5 9 C2 5.5 2 4 2 3.5 a3 3 0 0 1 6 0 C8 4 8 5.5 5 9Z"/></svg>Suite 4, 282 Falcon Street, Richmond, VIC 3121</li>
    <li><svg class="icon" viewBox="0 0 10 10"><path d="M2 1 L4 1 L5 3.5 L3.6 4.6 Q4.6 6.6 5.6 6.8 L6.6 5.6 L9 6.5 L9 8.6 Q5 9.5 2.5 6 Q0.8 3 2 1Z"/></svg>03 9417 2253</li>
    <li><svg class="icon" viewBox="0 0 10 10"><rect x="1" y="3.5" width="8" height="4.5" rx="1"/><rect x="3" y="1" width="4" height="2.5"/></svg>03 9417 2255</li>
    <li><svg class="icon" viewBox="0 0 10 10"><circle cx="5" cy="5" r="4"/><path d="M1 5H9M5 1Q2.5 5 5 9M5 1Q7.5 5 5 9"/></svg>www.drmaylacorwen.com.au</li>
    <li><svg class="icon" viewBox="0 0 10 10"><rect x="1" y="2" width="8" height="6"/><path d="M1 2L5 5.5L9 2"/></svg>admin@drmaylacorwen.com.au</li>
  </ul>
  <svg class="wave" style="height:80px" viewBox="0 0 400 100" preserveAspectRatio="none" aria-hidden="true">
    <path d="M0 48 C110 56 190 56 260 32 C320 10 370 0 400 4 V100 H0Z" fill="var(--plum)"/>
    <path d="M0 55 C110 62 200 64 270 44 C330 26 370 20 400 24 V100 H0Z" fill="var(--blue)"/>
  </svg>
</section>

<!-- envelope front -->
<section class="sheet envelope-front">
  <div class="brand" style="left:20px;top:113px;font-size:17px">Dr Mayla Corwen</div>
  <svg class="wave" style="height:80px" viewBox="0 0 400 100" preserveAspectRatio="none" aria-hidden="true">
    <path d="M0 48 C110 56 190 56 260 32 C320 10 370 0 400 4 V100 H0Z" fill="var(--plum)"/>
    <path d="M0 55 C110 62 200 64 270 44 C330 26 370 20 400 24 V100 H0Z" fill="var(--blue)"/>
  </svg>
</section>

<!-- business card front -->
<section class="sheet card-front">
  <div class="portrait" role="img" aria-label="Portrait photograph of the doctor"></div>
  <ul class="contact" style="left:136px;top:34px">
    <li><svg class="icon" viewBox="0 0 10 10"><path d="M2 1 L4 1 L5 3.5 L3.6 4.6 Q4.6 6.6 5.6 6.8 L6.6 5.6 L9 6.5 L9 8.6 Q5 9.5 2.5 6 Q0.8 3 2 1Z"/></svg>03 9417 2253</li>
    <li><svg class="icon" viewBox="0 0 10 10"><rect x="1" y="3.5" width="8" height="4.5" rx="1"/><rect x="3" y="1" width="4" height="2.5"/></svg>03 9417 2255</li>
    <li><svg class="icon" viewBox="0 0 10 10"><circle cx="5" cy="5" r="4"/><path d="M1 5H9M5 1Q2.5 5 5 9M5 1Q7.5 5 5 9"/></svg>www.drmaylacorwen.com.au</li>
    <li><svg class="icon" viewBox="0 0 10 10"><rect x="1" y="2" width="8" height="6"/><path d="M1 2L5 5.5L9 2"/></svg>admin@drmaylacorwen.com.au</li>
  </ul>
  <div class="brand" style="left:24px;top:77px;font-size:12px">Dr Mayla Corwen</div>
  <ul class="contact" style="left:24px;top:98px">
    <li><svg class="icon" viewBox="0 0 10 10"><path d="M5 9 C2 5.5 2 4 2 3.5 a3 3 0 0 1 6 0 C8 4 8 5.5 5 9Z"/></svg>Suite 4, 282 Falcon Street, Richmond, VIC 3121</li>
  </ul>
  <svg class="wave" style="height:46px" viewBox="0 0 400 100" preserveAspectRatio="none" aria-hidden="true">
    <path d="M0 54 C110 60 190 58 260 30 C320 6 370 0 400 8 V100 H0Z" fill="var(--plum)"/>
    <path d="M0 60 C110 66 200 64 270 40 C330 22 370 22 400 30 V100 H0Z" fill="var(--blue)"/>
  </svg>
</section>

<!-- business card back -->
<section class="sheet card-back">
  <svg style="position:absolute;left:0;top:0;width:105px;height:24px" viewBox="0 0 105 24" preserveAspectRatio="none" aria-hidden="true">
    <path d="M0 0 H105 C80 12 50 22 0 22Z" fill="var(--plum)"/>
    <path d="M0 0 H105 C80 8 50 14 0 13Z" fill="#fff"/>
    <path d="M0 0 H105 V0 H0Z" fill="#fff"/>
  </svg>
  <svg style="position:absolute;right:0;bottom:0;width:105px;height:24px" viewBox="0 0 105 24" preserveAspectRatio="none" aria-hidden="true">
    <path d="M0 24 C30 8 70 0 105 6 V24Z" fill="var(--blue)"/>
    <path d="M6 24 C40 12 75 8 105 12 V24Z" fill="#fff"/>
  </svg>
  <div class="brand" style="left:34px;top:54px;font-size:17px">Dr Mayla Corwen</div>
</section>

<!-- patient letterhead -->
<section class="sheet letter-patient">
  <div class="brand" style="left:21px;top:24px;font-size:16px">Dr Mayla Corwen</div>
  <div class="doctor-block" style="left:195px;top:20px">
    <div class="name">Dr Mayla Corwen</div>
    <div class="role" style="font-size:2.4px;line-height:3px">MBBS FRACP PhD</div>
    <div class="role">Consultant Endocrinologist</div>
  </div>
  <ul class="contact" style="left:195px;top:42px;line-height:5.6px">
    <li><svg class="icon" viewBox="0 0 10 10"><path d="M5 9 C2 5.5 2 4 2 3.5 a3 3 0 0 1 6 0 C8 4 8 5.5 5 9Z"/></svg>Suite 4, 282 Falcon Street,</li>
    <li style="padding-left:8px;margin-top:-2px">Richmond, VIC 3121</li>
    <li><svg class="icon" viewBox="0 0 10 10"><path d="M2 1 L4 1 L5 3.5 L3.6 4.6 Q4.6 6.6 5.6 6.8 L6.6 5.6 L9 6.5 L9 8.6 Q5 9.5 2.5 6 Q0.8 3 2 1Z"/></svg>03 9417 2253</li>
    <li><svg class="icon" viewBox="0 0 10 10"><rect x="1" y="3.5" width="8" height="4.5" rx="1"/><rect x="3" y="1" width="4" height="2.5"/></svg>03 9417 2255</li>
  </ul>
  <div class="patient-fields"><span>Patient</span><span class="line" style="flex:3"></span><span>Sex</span><span class="line"></span><span>Age</span><span class="line"></span></div>
  <ul class="contact" style="left:21px;top:346px;font-size:4px;line-height:7.6px">
    <li><svg class="icon" viewBox="0 0 10 10"><circle cx="5" cy="5" r="4"/><path d="M1 5H9M5 1Q2.5 5 5 9M5 1Q7.5 5 5 9"/></svg>www.drmaylacorwen.com.au</li>
    <li><svg class="icon" viewBox="0 0 10 10"><rect x="1" y="2" width="8" height="6"/><path d="M1 2L5 5.5L9 2"/></svg>admin@drmaylacorwen.com.au</li>
  </ul>
  <svg class="wave" style="height:58px" viewBox="0 0 400 100" preserveAspectRatio="none" aria-hidden="true">
    <path d="M0 56 C110 62 190 56 260 30 C320 8 370 0 400 6 V100 H0Z" fill="var(--plum)"/>
    <path d="M0 62 C110 68 200 66 270 42 C330 24 370 20 400 26 V100 H0Z" fill="var(--blue)"/>
  </svg>
</section>

<!-- general letterhead -->
<section class="sheet letter-general">
  <div class="brand" style="left:21px;top:23px;font-size:15px">Dr Mayla Corwen</div>
  <ul class="contact right" style="right:21px;top:20px">
    <li>03 9417 2253<svg class="icon" viewBox="0 0 10 10"><path d="M2 1 L4 1 L5 3.5 L3.6 4.6 Q4.6 6.6 5.6 6.8 L6.6 5.6 L9 6.5 L9 8.6 Q5 9.5 2.5 6 Q0.8 3 2 1Z"/></svg></li>
    <li>03 9417 2255<svg class="icon" viewBox="0 0 10 10"><rect x="1" y="3.5" width="8" height="4.5" rx="1"/><rect x="3" y="1" width="4" height="2.5"/></svg></li>
    <li>www.drmaylacorwen.com.au<svg class="icon" viewBox="0 0 10 10"><circle cx="5" cy="5" r="4"/><path d="M1 5H9M5 1Q2.5 5 5 9M5 1Q7.5 5 5 9"/></svg></li>
    <li>admin@drmaylacorwen.com.au<svg class="icon" viewBox="0 0 10 10"><rect x="1" y="2" width="8" height="6"/><path d="M1 2L5 5.5L9 2"/></svg></li>
  </ul>
  <div class="recipient" style="left:21px;top:94px"><div class="name">Dr Mayla Corwen</div><div class="role">Endocrinologist</div></div>
  <div class="date" style="right:21px;top:101px">Date : 06 May 2026</div>
  <div class="body-copy" style="left:21px;top:135px;width:234px">
    <p>Lorem ipsum dolor sit amet, consectetuer adipiscing elit, sed diam nonummy nibh euismod tincidunt ut laoreet dolore magna aliquam erat volutpat. Ut wisi enim ad minim veniam, quis nostrud exerci tation ullamcorper suscipit lobortis nisl ut aliquip ex ea commodo consequat. Duis autem vel eum iriure dolor in hendrerit in vulputate velit esse molestie consequat, vel illum dolore eu feugiat nulla facilisis at vero eros et accumsan et</p>
    <p>Lorem ipsum dolor sit amet, consectetuer adipiscing elit, sed diam nonummy nibh euismod tincidunt ut laoreet dolore magna aliquam erat volutpat. Ut wisi enim ad minim veniam, quis nostrud exerci tation ullamcorper suscipit lobortis nisl ut aliquip ex ea commodo consequat. Duis autem vel eum iriure dolor in hendrerit in vulputate velit esse molestie consequat, vel illum dolore eu feugiat nulla facilisis at vero eros et accumsan et</p>
  </div>
  <div class="signature" style="left:52px;top:268px;width:95px;height:18px" role="img" aria-label="Handwritten signature of Dr Mayla Corwen"></div>
  <div class="sign-role" style="left:52px;top:289px;width:95px">Endocrinologist</div>
  <svg style="position:absolute;left:68px;top:336px;width:7px;height:7px" viewBox="0 0 10 10" aria-hidden="true"><path d="M5 9 C2 5.5 2 4 2 3.5 a3 3 0 0 1 6 0 C8 4 8 5.5 5 9Z" fill="none" stroke="var(--blue)" stroke-width="1"/></svg>
  <div class="address-foot" style="left:20px;top:348px;width:110px">Suite 4, 282 Falcon Street,<br>Richmond, VIC 3121</div>
  <svg class="wave" style="height:58px" viewBox="0 0 400 100" preserveAspectRatio="none" aria-hidden="true">
    <path d="M0 56 C110 62 190 56 260 30 C320 8 370 0 400 6 V100 H0Z" fill="var(--plum)"/>
    <path d="M0 62 C110 68 200 66 270 42 C330 24 370 20 400 26 V100 H0Z" fill="var(--blue)"/>
  </svg>
</section>

<!-- presentation folder -->
<section class="sheet folder">
  <div class="brand" style="left:27px;top:34px;font-size:21px">Dr Mayla Corwen</div>

  <div class="folder-insert">
    <div class="brand" style="left:20px;top:22px;font-size:14px">Dr Mayla Corwen</div>
    <ul class="contact right" style="right:20px;top:20px;font-size:3.2px;line-height:6px">
      <li>03 9417 2253<svg class="icon" viewBox="0 0 10 10"><path d="M2 1 L4 1 L5 3.5 L3.6 4.6 Q4.6 6.6 5.6 6.8 L6.6 5.6 L9 6.5 L9 8.6 Q5 9.5 2.5 6 Q0.8 3 2 1Z"/></svg></li>
      <li>03 9417 2255<svg class="icon" viewBox="0 0 10 10"><rect x="1" y="3.5" width="8" height="4.5" rx="1"/><rect x="3" y="1" width="4" height="2.5"/></svg></li>
      <li>www.drmaylacorwen.com.au<svg class="icon" viewBox="0 0 10 10"><circle cx="5" cy="5" r="4"/><path d="M1 5H9M5 1Q2.5 5 5 9M5 1Q7.5 5 5 9"/></svg></li>
      <li>admin@drmaylacorwen.com.au<svg class="icon" viewBox="0 0 10 10"><rect x="1" y="2" width="8" height="6"/><path d="M1 2L5 5.5L9 2"/></svg></li>
    </ul>
    <div class="recipient" style="left:20px;top:88px;font-size:5px"><div class="name">Dr Mayla Corwen</div><div class="role" style="font-size:4px">Endocrinologist</div></div>
    <div class="date" style="right:20px;top:96px;font-size:3.8px">Date : 06 May 2026</div>
    <div class="body-copy" style="left:20px;top:128px;width:221px;font-size:4.2px;line-height:8.9px">
      <p>Lorem ipsum dolor sit amet, consectetuer adipiscing elit, sed diam nonummy nibh euismod tincidunt ut laoreet dolore magna aliquam erat volutpat. Ut wisi enim ad minim veniam, quis nostrud exerci tation ullamcorper suscipit lobortis nisl ut aliquip ex ea commodo consequat. Duis autem vel eum iriure dolor in hendrerit in vulputate velit esse molestie consequat, vel illum dolore eu feugiat nulla facilisis at vero eros et accumsan et</p>
      <p>Lorem ipsum dolor sit amet, consectetuer adipiscing elit, sed diam nonummy nibh euismod tincidunt ut laoreet dolore magna aliquam erat volutpat. Ut wisi enim ad minim veniam, quis nostrud exerci tation ullamcorper suscipit lobortis nisl ut aliquip ex ea commodo consequat. Duis autem vel eum iriure dolor in hendrerit in vulputate velit esse molestie consequat, vel illum dolore eu feugiat nulla facilisis at vero eros et accumsan et</p>
    </div>
    <div class="signature" style="left:50px;top:266px;width:90px;height:16px" role="img" aria-label="Handwritten signature of Dr Mayla Corwen"></div>
    <div class="sign-role" style="left:50px;top:285px;width:90px;font-size:5px">Endocrinologist</div>
  </div>

  <svg style="position:absolute;right:0;top:304px;width:21px;height:14px" viewBox="0 0 21 14" preserveAspectRatio="none" aria-hidden="true"><path d="M0 0 Q12 2 21 8 V14 H0Z" fill="var(--plum)"/></svg>
  <svg class="pocket-gap" viewBox="0 0 30 86" preserveAspectRatio="none" aria-hidden="true">
    <path d="M0 8 L30 0 L15 86Z" fill="var(--blue)"/>
    <path d="M0 8 L30 0 L29 5 L1 13Z" fill="var(--plum)"/>
  </svg>
  <div class="pocket pocket-left"></div>
  <div class="pocket pocket-right">
    <div class="brand" style="left:126px;top:45px;font-size:14px">Dr Mayla Corwen</div>
  </div>
</section>

</body>
</html>
```